Mark & Lisa's Hammock Season Party

Invitation to a party 60-80 people at a private residence. Age range 30-40s.

Themes: summer/casual/Australian backyard/local community

**For delivery via both email and printed copy**
Would like one document suitable for both purposes or two versions for electronic or paper invitation. I will arrange printing so please prepare it in a suitable format.

Specimen text attached. Address and phone contact to follow by message with successful bidder

Thanks!
Mark

Target Market(s)

Locals, friends. Party attendees will typicaly be parents in their forties who who be leaving the kids at home for a relaxed party night, and walking home afterward

Industry/Entity Type

Community

Font styles to use
Sans Serif

Requirements
Should not have
• Cliche Australiana imagery. No kangaroos etc

```html
<!DOCTYPE html>
<html lang="en">
<head>
<meta charset="utf-8">
<title>Mark &amp; Lisa's Hammock Season Party</title>
<link rel="stylesheet" href="https://fonts.googleapis.com/css2?family=Bodoni+Moda:opsz,wght@6..96,400&family=Montserrat:wght@600&display=swap">
<style>
  :root {
    --sky: #7ae1ee;
    --paper: #ffffff;
    --ink: #1f1f1f;
    --cloud-tint: rgba(122, 225, 238, 0.22);
  }
  * { box-sizing: border-box; margin: 0; padding: 0; }
  html, body { width: 1200px; height: 763px; overflow: hidden; }
  body { background: var(--sky); position: relative; }

  .invite-card {
    position: absolute;
    left: 38px; top: 36px;
    width: 1128px; height: 691px;
    background: var(--paper);
  }

  .host-names {
    position: absolute;
    top: 50px;
    height: 590px;
    width: 96px;
    display: flex;
    align-items: center;
    justify-content: center;
    writing-mode: vertical-rl;
    font-family: "Bodoni Moda", "Didot", serif;
    font-size: 66px;
    letter-spacing: 12px;
    color: var(--sky);
    white-space: nowrap;
    line-height: 1;
  }
  .host-names .amp { font-size: 124px; letter-spacing: 0; margin: 8px 0; }
  .host-names--left { left: 48px; }
  .host-names--right { right: 60px; transform: rotate(180deg); }

  .cloud-shape {
    position: absolute;
    left: 272px; top: 234px;
    width: 584px; height: 200px;
    border-radius: 100px 120px 90px 80px / 90px 100px 80px 70px;
    background: radial-gradient(ellipse at center, var(--cloud-tint), rgba(122, 225, 238, 0.08) 75%);
  }

  .details {
    position: absolute;
    left: 0; right: 0; top: 185px;
    text-align: center;
    color: var(--ink);
  }
  .caps {
    font-family: "Montserrat", "Helvetica Neue", sans-serif;
    font-weight: 600;
    text-transform: uppercase;
    font-size: 16px;
    letter-spacing: 3.2px;
    line-height: 21px;
  }
  .caps--small { font-size: 13px; letter-spacing: 3px; }
  .welcome {
    font-family: "Bodoni Moda", "Didot", serif;
    font-size: 25px;
    letter-spacing: 0.8px;
    line-height: 25px;
    margin-top: 19px;
  }
  .block-food { margin-top: 19px; }
  .rsvp { margin-top: 14px; }
  .contact-line { margin-top: 11px; }
  .contact-or { margin-top: 10px; }
  .contact-last { margin-top: 11px; }
</style>
</head>
<body>
  <main class="invite-card">
    <div class="host-names host-names--left">MARK <span class="amp">&amp;</span> LISA</div>
    <div class="host-names host-names--right">MARK <span class="amp">&amp;</span> LISA</div>

    <div class="cloud-shape" role="img" aria-label="Sky-blue outline of a drifting cloud behind the party details"></div>

    <section class="details">
      <p class="caps block-dress">Child-free event<br>Dress: summer casual, bare feet welcome</p>
      <p class="caps block-food">Cocktail food provided<br>BYO but only if you insist</p>
      <p class="welcome">If you have some friends or neighbours<br>that you like to hang out with,<br>We would love to meet. Bring them with you!</p>
      <p class="caps rsvp">An RSVP for catering would be nice.</p>
      <p class="caps caps--small contact-line">Text Mark 000 555 0148</p>
      <p class="caps caps--small contact-or">or</p>
      <p class="caps caps--small contact-last">Lisa 000 555 0162 before Xmas please.</p>
    </section>
  </main>
</body>
</html>
```